Real estate business needing a creative mind!

Have a real estate business called Brightwell Estates LLC. I need some business card with custom logo. That logo can be an intricate design of a house or houses. Maybe some blue and orange colors, maybe the business name in orange. Some thing that leaves a wow impression to the holder. Or just surprise me! Must have business name, name, email and phone number.

Target Market(s)

Property sellers and real estate professionals

Industry/Entity Type

Real estate

Contact Information for Business Card

Want it to stand out but also be professional.

Colors

Designer to choose colors to be used in the design.

Requirements
Must have
• Business name Brightwell Estates. My name which is Dalton Meese. The business email which is Brightwellestates1@novamail.example. The phone number which is 555-014-2297
Nice to have
• Could be a logo of the name over some mountain houses being that we live by the Smokey mountains. Could have a sun if it looks ok?

```html
<!DOCTYPE html>
<html lang="en">
<head>
<meta charset="utf-8">
<title>Brightwell Estates LLC — Business Card</title>
<link href="https://fonts.googleapis.com/css2?family=Montserrat:wght@400;600;800&display=swap" rel="stylesheet">
<style>
  :root {
    --navy: #0b2550;
    --navy-deep: #071c40;
    --orange: #f28a22;
    --white: #ffffff;
    --paper: #fbfbfb;
    --backdrop: #3a3a3c;
    --divider: rgba(255, 255, 255, 0.28);
  }
  * { box-sizing: border-box; margin: 0; padding: 0; }
  html, body {
    width: 1200px;
    height: 1200px;
    overflow: hidden;
    background: var(--backdrop);
    font-family: "Montserrat", sans-serif;
  }
  .stage {
    width: 1200px;
    height: 1200px;
    display: flex;
    flex-direction: column;
    align-items: center;
    justify-content: center;
    gap: 70px;
  }
  .card {
    position: relative;
    width: 700px;
    height: 400px;
    border-radius: 28px;
    overflow: hidden;
    box-shadow: 0 18px 40px rgba(0, 0, 0, 0.45);
  }

  /* Front */
  .card-front { background: var(--paper); }
  .front-band {
    position: absolute;
    left: 0; right: 0; bottom: 0;
    height: 172px;
    background: var(--navy);
  }
  .front-rule {
    position: absolute;
    left: 0; right: 0;
    bottom: 182px;
    height: 6px;
    background: var(--orange);
  }
  .front-brand {
    position: absolute;
    top: 0; left: 0; right: 0;
    height: 218px;
    display: flex;
    align-items: center;
    justify-content: center;
  }
  .brand-name {
    font-weight: 800;
    letter-spacing: 1px;
    text-transform: uppercase;
    text-align: center;
    line-height: 1.1;
  }
  .front-brand .brand-name {
    color: var(--navy);
    font-size: 34px;
  }
  .agent {
    position: absolute;
    left: 48px;
    bottom: 46px;
  }
  .agent-name {
    color: var(--orange);
    font-size: 27px;
    font-weight: 600;
    text-transform: uppercase;
    letter-spacing: 0.5px;
  }
  .agent-title {
    color: var(--white);
    font-size: 14px;
    font-weight: 400;
    text-transform: uppercase;
    letter-spacing: 1px;
    margin-top: 2px;
  }
  .band-divider {
    position: absolute;
    left: 330px;
    bottom: 38px;
    width: 1px;
    height: 96px;
    background: var(--divider);
  }
  .contact {
    position: absolute;
    left: 360px;
    bottom: 62px;
    list-style: none;
    color: var(--white);
    font-size: 14px;
  }
  .contact li {
    display: flex;
    align-items: center;
    gap: 10px;
    margin: 8px 0;
  }
  .contact svg { width: 16px; height: 16px; flex: none; }

  /* Back */
  .card-back {
    background: linear-gradient(135deg, var(--navy-deep), var(--navy) 60%, #12305f);
    display: flex;
    align-items: center;
    justify-content: center;
  }
  .card-back .brand-name {
    color: var(--white);
    font-size: 46px;
  }
</style>
</head>
<body>
<main class="stage">

  <section class="card card-front" aria-label="Business card front">
    <div class="front-brand">
      <p class="brand-name">Brightwell Estates LLC</p>
    </div>
    <div class="front-rule"></div>
    <div class="front-band"></div>
    <div class="agent">
      <p class="agent-name">Dalton Meese</p>
      <p class="agent-title">Real Estate Agent</p>
    </div>
    <div class="band-divider"></div>
    <ul class="contact">
      <li>
        <svg viewBox="0 0 24 24" aria-hidden="true"><path fill="#f28a22" d="M6.6 10.8a15.1 15.1 0 0 0 6.6 6.6l2.2-2.2a1 1 0 0 1 1-.25 11.4 11.4 0 0 0 3.6.57 1 1 0 0 1 1 1V20a1 1 0 0 1-1 1A17 17 0 0 1 3 4a1 1 0 0 1 1-1h3.5a1 1 0 0 1 1 1c0 1.25.2 2.45.57 3.6a1 1 0 0 1-.25 1z"/></svg>
        <span>555-014-2297</span>
      </li>
      <li>
        <svg viewBox="0 0 24 24" aria-hidden="true"><path fill="#f28a22" d="M2 5h20v14H2z"/><path fill="none" stroke="#0b2550" stroke-width="1.8" d="M2 5l10 8 10-8M2 19l7.5-7M22 19l-7.5-7"/></svg>
        <span>brightwellestates1@novamail.example</span>
      </li>
    </ul>
  </section>

  <section class="card card-back" aria-label="Business card back">
    <p class="brand-name">Brightwell<br>Estates LLC</p>
  </section>

</main>
</body>
</html>
```